Bible Word Search Activity Book Series

The design will be used across a series (3) of Word Search puzzle books on the Bibile: The Holy Bible Volume 1, The Book Of Psalms Volume 1, and the Book Of Proverbs Volume 1. The design can be the same on all three books the titles will of course just need to be different (open to creative suggestions here.) Some ideas for the titles of each include: “Bible Word Search Large Print Puzzles For Adults and Kids Volume 1,” and/or “Book Of Psalms Word Search Large Print Volume 1” etc.

Target Market(s)

Adults middle age and older and kids. The three books might also be used for a biblical word association study aid. This will be a printed book targeting those that have an interest in printed activity books and biblical study material and may want an alternative to games on electronic devices like Lumetabs.

Industry/Entity Type

Games

Font styles to use
Serif
Script

Colors

Designer to choose colors to be used in the design.

Requirements
Must have
• Most of the printed puzzle and activity books that are available today, with the exception of those published by The Harrowgate Courier are very dry would like to see something unique and eye catching with a clear title.
Nice to have
• Would be nice to perhaps have a bible somewhere in the cover design. Possible idea might be a silhouette of a person looking in to or reading the Bible. I've attached some designs from current puzzle books that have caught my attention. Design might incorporate something biblical but it doesn't necessarily have to. Would like to see the use of some color in the design.

```html
<!DOCTYPE html>
<html lang="en">
<head>
<meta charset="utf-8">
<title>Bible Word Search Puzzle Books – Book of Psalms, Volume 1</title>
<link href="https://fonts.googleapis.com/css2?family=Amatic+SC:wght@400;700&family=Playball&display=swap" rel="stylesheet">
<style>
  :root {
    --band-purple: #7f74b6;
    --title-white: #f7f5fb;
    --title-yellow: #f3c533;
    --tag-yellow: #f1c02c;
    --tag-ink: #1f1c22;
    --floral-olive: #8f9550;
    --floral-leaf: #5f6a35;
    --floral-lilac: #8a7fc0;
    --floral-cream: #f1ecb4;
    --floral-gold: #e3b838;
  }
  html, body {
    margin: 0;
    padding: 0;
    width: 800px;
    height: 1200px;
    overflow: hidden;
    background: var(--floral-olive);
  }
  .cover {
    position: relative;
    width: 800px;
    height: 1200px;
    overflow: hidden;
  }
  .floral-field {
    position: absolute;
    left: 0;
    width: 800px;
  }
  .floral-field--top {
    top: 0;
    height: 207px;
    background:
      radial-gradient(circle at 18% 60%, var(--floral-cream) 0 9%, transparent 24%),
      radial-gradient(circle at 48% 45%, var(--floral-lilac) 0 10%, transparent 26%),
      radial-gradient(circle at 80% 40%, var(--floral-cream) 0 8%, transparent 22%),
      radial-gradient(circle at 95% 70%, var(--floral-gold) 0 6%, transparent 18%),
      linear-gradient(180deg, var(--floral-olive), var(--floral-leaf));
  }
  .floral-field--bottom {
    top: 611px;
    height: 589px;
    background:
      radial-gradient(circle at 20% 12%, var(--floral-cream) 0 8%, transparent 18%),
      radial-gradient(circle at 58% 30%, var(--floral-lilac) 0 9%, transparent 20%),
      radial-gradient(circle at 22% 50%, var(--floral-cream) 0 9%, transparent 20%),
      radial-gradient(circle at 85% 45%, var(--floral-lilac) 0 10%, transparent 22%),
      radial-gradient(circle at 40% 85%, var(--floral-cream) 0 8%, transparent 20%),
      radial-gradient(circle at 80% 90%, var(--floral-gold) 0 7%, transparent 18%),
      radial-gradient(circle at 8% 80%, var(--floral-lilac) 0 7%, transparent 18%),
      linear-gradient(180deg, var(--floral-olive), var(--floral-leaf));
  }
  .title-band {
    position: absolute;
    left: 0;
    top: 207px;
    width: 800px;
    height: 404px;
    background: var(--band-purple);
    text-align: center;
  }
  .series-line {
    position: absolute;
    top: 28px;
    left: 0;
    width: 100%;
    margin: 0;
    font-family: "Amatic SC", cursive;
    font-weight: 400;
    font-size: 86px;
    line-height: 1;
    letter-spacing: 4px;
    color: var(--title-white);
  }
  .series-title {
    position: absolute;
    top: 110px;
    left: 0;
    width: 100%;
    margin: 0;
    font-family: "Amatic SC", cursive;
    font-weight: 400;
    font-size: 138px;
    line-height: 1;
    letter-spacing: 6px;
    color: var(--title-yellow);
  }
  .divider {
    position: absolute;
    top: 270px;
    left: 56px;
    width: 688px;
    height: 16px;
  }
  .book-name {
    position: absolute;
    top: 298px;
    left: 0;
    width: 100%;
    margin: 0;
    font-family: "Playball", cursive;
    font-weight: 400;
    font-size: 72px;
    line-height: 1;
    color: var(--title-yellow);
  }
  .volume-tag {
    position: absolute;
    left: 537px;
    top: 611px;
    width: 263px;
    height: 70px;
    background: var(--tag-yellow);
    font-family: "Amatic SC", cursive;
    font-weight: 400;
    font-size: 62px;
    line-height: 70px;
    letter-spacing: 3px;
    color: var(--tag-ink);
    padding-left: 26px;
    box-sizing: border-box;
  }
</style>
</head>
<body>
  <main class="cover">
    <div class="floral-field floral-field--top" role="img" aria-label="Spring flowers: primroses, daisies and bluebells in cream, yellow and lilac among olive leaves"></div>

    <section class="title-band">
      <p class="series-line">Bible Word Search</p>
      <h1 class="series-title">Puzzle Books</h1>
      <svg class="divider" viewBox="0 0 688 16" aria-hidden="true">
        <line x1="0" y1="8" x2="300" y2="8" stroke="#f7f5fb" stroke-width="2"/>
        <line x1="388" y1="8" x2="688" y2="8" stroke="#f7f5fb" stroke-width="2"/>
        <circle cx="344" cy="8" r="5" fill="#f7f5fb"/>
      </svg>
      <h2 class="book-name">Book of Psalms</h2>
    </section>

    <div class="floral-field floral-field--bottom" role="img" aria-label="Spring flowers: primroses, daisies, grape hyacinths and cornflowers in cream, yellow and purple among olive leaves"></div>

    <div class="volume-tag">Volume 1</div>
  </main>
</body>
</html>
```